CPA Graduation Party

I need to make simple invitation for my sister's recent success, passing the CPA (Certified Public Accountant) exam. It is a surprise party. I want very simple and professional looking invitation. My only requirements are that you don't use any graduation caps or gowns due to the fact that it's not an actual graduation. It's a series of exams that she passes. Be creative with the design but once again, keep it professional. I have attached a font called iScriptSTD. I liked the font so was thinking about using it. But it's not necessary. If you have something slimier or better, please use it.

I was planning on printing on a specific kind of paper. It's called pearlized ivory cardstock. It has a little coating and shine on it and since it's ivory, I was thinking about the main color of the invitation to be burgundy type. For example, see the following RGB: R204, G0, B102.

Party info:
Name: Ravina
Date & Time: Saturday, March 8th, 2014 at 6:00pm
Location: Seher Mahal. 418 Brambleford Lane Parsippany, NJ 07291

I know I didn't provide a lot of info for the invite but please be creative.  Use general knowledge and other formal party invites as examples. I am not looking for a name, date and location as three bullets on the card.

Also, I forgot to mention the size of the invite.  It should be 5.5x8.5.  Thank you.

• graduation caps and/or gowns

```html
<!DOCTYPE html>
<html lang="en">
<head>
<meta charset="utf-8">
<title>Celebration Party of Ravina</title>
<link rel="stylesheet" href="https://fonts.googleapis.com/css2?family=Oregano&display=swap">
<style>
  :root {
    --page: #ffffff;
    --card: #f0f0f0;
    --magenta: #cc0066;
    --band: #aa0066;
    --fold: #700042;
    --ribbon-text: #ffffff;
  }
  * { margin: 0; padding: 0; box-sizing: border-box; }
  html, body {
    width: 1200px;
    height: 1000px;
    overflow: hidden;
    background: var(--page);
  }
  .invitation {
    position: absolute;
    left: 117px;
    top: 176px;
    width: 959px;
    height: 620px;
    background: var(--card);
    font-family: "Oregano", cursive;
    color: var(--magenta);
  }
  .header-ribbon {
    position: absolute;
    left: 0;
    top: 70px;
    width: 959px;
    height: 59px;
  }
  .header-ribbon__label {
    position: absolute;
    left: 345px;
    top: 70px;
    width: 286px;
    height: 43px;
    line-height: 43px;
    text-align: center;
    font-size: 27px;
    color: var(--ribbon-text);
  }
  .line {
    position: absolute;
    left: 0;
    width: 100%;
    text-align: center;
    white-space: nowrap;
  }
  .line--of { top: 120px; font-size: 27px; }
  .line--name { top: 160px; font-size: 80px; letter-spacing: 1px; }
  .line--date { top: 330px; font-size: 28px; }
  .line--venue { top: 440px; font-size: 28px; }
  .tag {
    position: absolute;
    left: 423px;
    width: 137px;
    height: 40px;
  }
  .tag--on { top: 273px; }
  .tag--at { top: 384px; }
  .tag__label {
    position: absolute;
    left: 32px;
    top: 0;
    width: 73px;
    height: 29px;
    line-height: 30px;
    text-align: center;
    font-size: 20px;
    color: var(--ribbon-text);
  }
  .footer-band {
    position: absolute;
    left: 0;
    top: 517px;
    width: 959px;
    height: 43px;
    background: var(--magenta);
  }
</style>
</head>
<body>
<main class="invitation">
  <svg class="header-ribbon" viewBox="0 0 959 59" aria-hidden="true">
    <rect x="0" y="17" width="401" height="42" fill="var(--band)"/>
    <rect x="575" y="17" width="384" height="42" fill="var(--band)"/>
    <polygon points="345,43 401,43 401,59" fill="var(--fold)"/>
    <polygon points="575,43 631,43 575,59" fill="var(--fold)"/>
    <rect x="345" y="0" width="286" height="43" fill="var(--magenta)"/>
  </svg>
  <p class="header-ribbon__label">Celebration Party</p>

  <p class="line line--of">Of</p>
  <h1 class="line line--name" style="font-weight:400">RAVINA</h1>

  <div class="tag tag--on">
    <svg width="137" height="40" viewBox="0 0 137 40" aria-hidden="true">
      <polygon points="0,11 54,11 54,40 0,40 14,25" fill="var(--band)"/>
      <polygon points="137,11 83,11 83,40 137,40 123,25" fill="var(--band)"/>
      <polygon points="32,29 54,29 54,40" fill="var(--fold)"/>
      <polygon points="105,29 83,29 83,40" fill="var(--fold)"/>
      <rect x="32" y="0" width="73" height="29" fill="var(--magenta)"/>
    </svg>
    <span class="tag__label">On</span>
  </div>

  <p class="line line--date">Saturday, March 8th, 2014 at 6.00 pm</p>

  <div class="tag tag--at">
    <svg width="137" height="40" viewBox="0 0 137 40" aria-hidden="true">
      <polygon points="0,11 54,11 54,40 0,40 14,25" fill="var(--band)"/>
      <polygon points="137,11 83,11 83,40 137,40 123,25" fill="var(--band)"/>
      <polygon points="32,29 54,29 54,40" fill="var(--fold)"/>
      <polygon points="105,29 83,29 83,40" fill="var(--fold)"/>
      <rect x="32" y="0" width="73" height="29" fill="var(--magenta)"/>
    </svg>
    <span class="tag__label">At</span>
  </div>

  <p class="line line--venue">Seher Mahal, 418 Brambleford Lane Parsippany, NJ 07291</p>

  <div class="footer-band"></div>
</main>
</body>
</html>
```